Free Range Egg Farmer wants a Egg Carton Design

We need a design for Free Range Egg carton. Our company name is "BrookHaven The Craft of Growing"

We run a environmentally friendly farm in Gippsland VIC and we produce Free Range Eggs and Pasture Fed Meats in open pasture.

We also run a farm stay business in a very high energy star rating house.
The farm guest participates in our farm activity such as looking after farm animals, maintaining the vegetable garden, cooking fresh food, Yoga and Meditation.

We would like to see designs with our logo and something alternative rather than a typical free range egg cartons.

The team had a meeting and came up with one idea.
"The meditating hen" with thought bubble which we can change the hen's thought by printing batch.
You could either use this idea or create your own.

I have attached 3 photos close to my image as examples.
I also have attached the typical free range egg cartons as examples.

Sticker size is attached. The sticker fits between the case closure system. So there is no need to make spaces for the closure gaps.
Please place Best Before stamp area at the top right corner of the main (middle) section.
Updates

I have post an update to my brief. Please have a look again. BrookHaven

Industry/Entity Type

Printing

Requirements
Must have
• Company name,
Address,
contact number,
facebook logo,
best before date (space to put the stamp on)
12 Free Range Eggs xxx g
Nutrition info

```html
<!DOCTYPE html>
<html lang="en">
<head>
<meta charset="utf-8">
<title>BrookHaven – Organic Free Range Eggs Carton Sticker</title>
<link rel="stylesheet" href="https://fonts.googleapis.com/css2?family=Arimo:ital,wght@0,400;0,700;1,700&family=Tinos:wght@400&display=swap">
<style>
:root{
  --ink:#1a1a1a;
  --red:#e2231a;
  --deep-red:#c0161b;
  --leaf:#6fae2e;
  --leaf-dark:#3f7a1e;
  --leaf-pale:#eef6d8;
  --leaf-mid:#b9da6a;
  --cream:#fbfdf3;
  --panel-dark:#111111;
  --egg:#e8c9ad;
  --rule:#bdbdbd;
  --white:#ffffff;
}
*{box-sizing:border-box;margin:0;padding:0}
html,body{width:1200px;height:1058px;overflow:hidden;background:var(--white)}
body{position:relative;font-family:"Arimo",Arial,sans-serif;color:var(--ink)}
.abs{position:absolute}

/* ---------- panels ---------- */
.panel{position:absolute;border:1px solid var(--rule);overflow:hidden}
.flap-top{left:88px;top:10px;width:1100px;height:280px;transform:rotate(180deg);
  background:linear-gradient(100deg,var(--leaf-mid) 0%,var(--leaf-pale) 40%,var(--cream) 70%,var(--leaf-pale) 100%)}
.face{left:88px;top:300px;width:1100px;height:495px;background:var(--cream)}
.flap-bottom{left:88px;top:812px;width:1100px;height:213px;
  background:linear-gradient(90deg,var(--white) 0%,var(--cream) 30%,var(--leaf-pale) 70%,var(--leaf-mid) 100%)}

/* ---------- top flap (laid out upright, panel rotated) ---------- */
.nutrition-box{left:762px;top:78px;width:314px;height:196px;background:var(--white);border:2px solid var(--ink)}
.nutrition-box span{position:absolute;left:12px;top:6px;font-size:12px}
.mini-heading{left:110px;top:52px;font-size:34px;font-weight:700;white-space:nowrap}
.mini-heading .num{color:var(--red);font-size:40px}
.mini-heading .free{color:var(--red);font-style:italic}
.address{left:200px;top:118px;width:500px;font-size:12px;line-height:15px;color:#333}
.thumb{left:0;top:100px;width:188px;height:178px;background:var(--white);border-right:1px solid var(--rule)}
.thumb .band{position:absolute;left:0;top:0;width:100%;height:32px;background:var(--leaf-dark);color:var(--white);font-size:10px;font-style:italic;font-weight:700;padding:9px 0 0 46px}
.thumb .dot{position:absolute;left:12px;top:4px;width:24px;height:24px;border-radius:50%;background:var(--panel-dark);border:2px solid var(--leaf)}
.thumb .art{position:absolute;left:6px;top:40px;width:176px;height:130px;background:linear-gradient(160deg,#f6e6d6,var(--egg))}

/* ---------- main face ---------- */
.brand-col{left:0;top:0;width:350px;height:495px;background:var(--panel-dark)}
.logo-ring{left:112px;top:15px;width:124px;height:124px;border-radius:50%;background:#2c4a2a;border:4px solid var(--leaf)}
.logo-name{left:0;top:140px;width:350px;text-align:center;color:var(--white);font-size:18px;font-weight:700;letter-spacing:1px}
.tagline{left:0;top:172px;width:350px;height:46px;background:linear-gradient(90deg,#4c7f22,var(--leaf));color:var(--white);
  font-style:italic;font-weight:700;font-size:22px;padding:10px 0 0 22px}
.hen-scene{left:0;top:218px;width:432px;height:212px;background:linear-gradient(170deg,#fffaf3 0%,var(--egg) 70%,#d9ae86 100%)}
.weight-strip{left:0;top:430px;width:350px;height:65px;background:linear-gradient(90deg,#3f6f1a,#79a52d)}
.weight{left:190px;top:452px;color:var(--white);font-size:18px;font-weight:700;white-space:nowrap}
.seal-plain{left:12px;top:352px;width:76px;height:76px;border-radius:50%;background:var(--red);border:4px solid var(--white)}

.leaves{left:350px;top:0;width:750px;height:495px;background:
  radial-gradient(ellipse at 85% 15%,var(--leaf-mid) 0%,transparent 55%),
  radial-gradient(ellipse at 15% 85%,#d7ebaa 0%,transparent 50%),
  linear-gradient(120deg,var(--cream),var(--leaf-pale))}
.best-before{left:718px;top:18px;font-family:"Tinos",serif;font-size:17px}
.thumb-icon{left:368px;top:47px;width:48px;height:48px}
.headline{left:428px;top:44px;font-size:46px;font-weight:700;white-space:nowrap;letter-spacing:-.5px}
.headline .free{color:var(--red)}
.blurb{left:470px;top:108px;width:560px;font-family:"Tinos",serif;font-size:15.5px;line-height:19px;text-align:center}
.checks{left:610px;top:190px;list-style:none}
.checks li{position:relative;padding-left:40px;color:var(--deep-red);font-weight:700;font-size:15px;line-height:18px;margin-bottom:16px;width:230px}
.checks svg{position:absolute;left:0;top:-2px}
.facts{left:660px;top:428px;display:flex;gap:8px}
.fact{width:38px;height:38px;border-radius:50%;background:#dfe9f4;border:2px solid #8aa6c8;font-size:10px;font-weight:700;text-align:center;line-height:34px;color:#24456e}
.grade{left:975px;top:405px;width:70px;text-align:center}
.grade .word{font-size:13px;font-weight:700;letter-spacing:2px}
.grade .letter{margin:2px auto 0;width:46px;height:46px;border-radius:50%;border:3px solid var(--ink);background:var(--white);font-size:30px;font-weight:700;line-height:40px}

/* ---------- bottom flap ---------- */
.mini-logo{left:0;top:0;width:82px;height:78px;background:var(--panel-dark)}
.mini-logo .dot{position:absolute;left:17px;top:8px;width:48px;height:48px;border-radius:50%;background:#2c4a2a;border:3px solid var(--leaf)}
.mini-logo span{position:absolute;left:0;top:60px;width:82px;text-align:center;color:var(--white);font-size:9px;font-weight:700}
.flap-scene{left:90px;top:8px;width:252px;height:200px;background:linear-gradient(170deg,#fff8ee,var(--egg))}
.flap-heading{left:344px;top:38px;font-size:40px;font-weight:700;white-space:nowrap;letter-spacing:-.5px}
.flap-heading .num{color:var(--red);font-size:46px}
.flap-heading .free{color:var(--red)}
.flap-blurb{left:346px;top:100px;width:470px;font-family:"Tinos",serif;font-size:15px;line-height:18px;text-align:center}
.flap-seal{left:912px;top:36px;width:116px;height:116px;border-radius:50%;background:var(--deep-red);border:5px solid var(--white);box-shadow:0 0 0 2px var(--deep-red)}
.flap-weight{left:960px;top:168px;font-size:17px;font-weight:700}
</style>
</head>
<body>

<!-- top flap (printed upside down) -->
<section class="panel flap-top" aria-label="Top flap">
  <div class="abs thumb">
    <div class="band">The Craft of Growing</div>
    <div class="dot"></div>
    <div class="art" role="img" aria-label="Eggs in a nest"></div>
  </div>
  <div class="abs mini-heading"><span class="num">12</span> Organic <span class="free">FREE</span> range eggs</div>
  <p class="abs address">Address: 14 Ridgeway Lane, Mirboo Valley VIC 3871<br>Phone: 03 5550 1427 &nbsp; Email: hello@brookhaven.example<br>Keep refrigerated below 5°C. Packed on our family farm.</p>
  <div class="abs nutrition-box"><span>Nutrition Information</span></div>
</section>

<!-- main face -->
<section class="panel face" aria-label="Main face">
  <div class="abs leaves" role="img" aria-label="Soft green leaves background"></div>
  <div class="abs brand-col"></div>
  <div class="abs logo-ring"></div>
  <div class="abs logo-name">BrookHaven</div>
  <div class="abs tagline">The Craft of Growing</div>
  <div class="abs hen-scene" role="img" aria-label="Cartoon hen waving beside a pile of eggs"></div>
  <div class="abs weight-strip"></div>
  <div class="abs weight">700g XLarge</div>
  <div class="abs seal-plain" aria-hidden="true"></div>

  <div class="abs best-before">Best Before :</div>
  <svg class="abs thumb-icon" viewBox="0 0 48 48" aria-hidden="true">
    <circle cx="24" cy="24" r="23" fill="var(--red)"/>
    <path d="M13 22h6v14h-6zM21 22l5-10c3 0 4 2 3 5l-1 4h7c2 0 3 2 2 4l-3 9c-1 2-2 2-4 2H21z" fill="#fff"/>
  </svg>
  <h1 class="abs headline">Organic <span class="free">FREE</span> range eggs</h1>
  <p class="abs blurb">These Fresh, free range come to you from our accredited FREE range farms. Our healthy hens roam freely over pastures and are fed with wholesome mix if natural grains 100% free of animals protein. Enjoy!</p>
  <ul class="abs checks">
    <li><svg width="28" height="24" viewBox="0 0 28 24"><path d="M3 12l7 8L25 3" stroke="var(--red)" stroke-width="5" fill="none"/></svg>Hens roam freely over natural pastures</li>
    <li><svg width="28" height="24" viewBox="0 0 28 24"><path d="M3 12l7 8L25 3" stroke="var(--red)" stroke-width="5" fill="none"/></svg>Food is free of animal protein</li>
    <li><svg width="28" height="24" viewBox="0 0 28 24"><path d="M3 12l7 8L25 3" stroke="var(--red)" stroke-width="5" fill="none"/></svg>Hens fed natural grains</li>
    <li><svg width="28" height="24" viewBox="0 0 28 24"><path d="M3 12l7 8L25 3" stroke="var(--red)" stroke-width="5" fill="none"/></svg>Eggs are naturally free of hormones &amp; antibiotics</li>
  </ul>
  <div class="abs facts">
    <div class="fact">95</div><div class="fact">7%</div><div class="fact">7.0g</div><div class="fact">1%</div><div class="fact">1.9g</div><div class="fact">0.2g</div>
  </div>
  <div class="abs grade"><div class="word">GRADE</div><div class="letter">A</div></div>
</section>

<!-- bottom flap -->
<section class="panel flap-bottom" aria-label="Bottom flap">
  <div class="abs mini-logo"><div class="dot"></div><span>BrookHaven</span></div>
  <div class="abs flap-scene" role="img" aria-label="Cartoon hen with eggs"></div>
  <h2 class="abs flap-heading"><span class="num">12</span> Organic <span class="free">FREE</span> range eggs</h2>
  <p class="abs flap-blurb">These Fresh, free range come to you from our accredited FREE range farms. Our healthy hens roam freely over pastures and are fed with wholesome mix if natural grains 100% free of animals protein. Enjoy!</p>
  <div class="abs flap-seal" aria-hidden="true"></div>
  <div class="abs flap-weight">700g XLarge</div>
</section>

</body>
</html>
```